About the book: It is an A5 size book, small 40 pages miniguide
Book title: The pocket handbook of home lending
Book subtitle: The quiet road to plenty
Author: Ned Pargiter
Back cover content: Please see attached word document "back page"
Colours: Our company logo should go at the back of the book. One colour we can't use is red. As this is a finance book the red colour is seen negatively. may be light green? you are the expert.
I think lots of white space will work well.
NOTE: please read the back cover notes to get an understanding of what the book is about. It educates readers about finance in property investing. It makes sense that image used combines 'property' and 'finance'. please read back page document attached.
NOTE: it is a small A5 , 40 page book . Its a miniguide rather than a book .

Reason: Dear designers, Thank you for submitting your work over the last few days. Unfortunately we haven't been able to get back to you regarding the final selection of design as the Author of the book has been away on leave with his family without reliable internet access. He is now back and will be giving feedback as we go. We apologise for the time extension. Unfortunately the site didn’t allow me to limit the extension for less than 5 days but we may not require that long. Thanks again. Lulu

Reason: We apologies we hadn't finalized a decision on this project due to the person from our end being away. We would like to finalise this design as soon as possible.

Target Market(s)

22 - 45 age group. Most fall between 30-40. Both male and female. couples , individuals etc ...

Industry/Entity Type

Finance

Font styles to use
Other font styles liked:
• sabon/Aeriel. Let me know if any other suggestions.

Requirements
Nice to have
• use green colour if possible but not essential.

```html
<!DOCTYPE html>
<html lang="en">
<head>
<meta charset="utf-8">
<title>The pocket handbook of home lending — cover spread</title>
<link rel="stylesheet" href="https://fonts.googleapis.com/css2?family=Anton&family=Source+Sans+3:wght@400;600;700&display=swap">
<style>
  :root {
    --backdrop: #3d3d3f;
    --paper: #ffffff;
    --ink: #111111;
    --body-ink: #1c1c1c;
    --brand-green: #0a6b3a;
    --leaf-light: #9fdb9f;
    --leaf-mid: #4cb84f;
    --spine: #e4e4e4;
  }
  * { margin: 0; padding: 0; box-sizing: border-box; }
  html, body {
    width: 1200px; height: 999px; overflow: hidden;
    background: var(--backdrop);
  }
  .spread {
    position: absolute; left: 32px; top: 110px;
    width: 1136px; height: 778px;
    background: var(--paper);
    overflow: hidden;
  }
  .spine {
    position: absolute; left: 585px; top: 0; width: 1px; height: 100%;
    background: var(--spine);
  }
  .title-kicker {
    font-family: "Anton", "Impact", sans-serif;
    color: var(--brand-green);
    white-space: nowrap;
  }
  .title-main {
    font-family: "Anton", "Impact", sans-serif;
    color: var(--ink);
  }
  .illustration {
    position: absolute;
    background: radial-gradient(closest-side, var(--leaf-mid) 0%, var(--leaf-light) 55%, rgba(255,255,255,0) 100%);
  }

  /* back cover */
  .back-title { position: absolute; left: 199px; top: 33px; }
  .back-title .title-kicker { font-size: 14px; line-height: 18px; }
  .back-title .title-main { font-size: 44px; line-height: 44px; }
  .back-illustration { left: 46px; top: 122px; width: 150px; height: 116px; }
  .blurb {
    position: absolute; left: 46px; top: 244px; width: 459px;
    font-family: "Source Sans 3", Arial, sans-serif;
    font-size: 12px; line-height: 17px; color: var(--body-ink);
  }
  .blurb p { margin-bottom: 8px; }
  .lessons-heading {
    font-weight: 700; font-size: 14px; margin: 14px 0 8px 3px;
  }
  .lessons { list-style: none; text-align: justify; }
  .lessons li {
    position: relative; padding-left: 37px; margin-bottom: 9px;
  }
  .lessons li::before {
    content: ""; position: absolute; left: 4px; top: 6px;
    width: 6px; height: 6px; border-radius: 50%;
    background: var(--brand-green);
  }
  .publisher {
    position: absolute; left: 48px; top: 615px;
    display: flex; align-items: center; gap: 6px;
    font-family: "Source Sans 3", Arial, sans-serif;
    font-size: 14px; font-weight: 700; color: var(--brand-green);
  }
  .publisher-dot {
    width: 12px; height: 12px; border-radius: 50%; background: var(--brand-green);
  }

  /* band */
  .band {
    position: absolute; left: 0; top: 659px; width: 100%; height: 36px;
    background: var(--brand-green);
    color: var(--paper);
  }
  .contact {
    position: absolute; top: 0; line-height: 36px;
    font-family: "Source Sans 3", Arial, sans-serif; font-size: 15px;
  }
  .contact.phone { left: 98px; }
  .contact.web { left: 232px; }
  .tagline {
    position: absolute; left: 586px; width: 550px; top: 0;
    line-height: 34px; text-align: center;
    font-family: "Source Sans 3", Arial, sans-serif; font-weight: 400;
    font-size: 28px;
  }

  /* front cover */
  .front-title {
    position: absolute; left: 586px; width: 550px; top: 32px; text-align: center;
  }
  .front-title .title-kicker { font-size: 33px; line-height: 40px; }
  .front-title .title-main { font-size: 132px; line-height: 126px; margin-top: 8px; }
  .front-illustration { left: 586px; top: 340px; width: 440px; height: 300px; }
  .author {
    position: absolute; left: 586px; width: 550px; top: 700px; text-align: center;
    font-family: "Anton", "Impact", sans-serif; font-size: 44px; line-height: 56px; color: var(--ink);
  }
</style>
</head>
<body>
<main class="spread">
  <div class="spine"></div>

  <section class="back-cover">
    <div class="back-title">
      <div class="title-kicker">The pocket handbook of</div>
      <div class="title-main">home<br>lending</div>
    </div>
    <div class="illustration back-illustration" role="img" aria-label="Green 3D house outline turning into a rising arrow"></div>

    <div class="blurb">
      <p>The number-one reason most investors never own more than one property is finance. For them, getting and managing money is the scariest part of investing.</p>
      <p>You must be 100% informed when structuring your loans. Before you even think about finding a property, you must understand the valuation process.</p>
      <p>In simple, jargon-free language, this mini guide arms you with a wealth of knowledge to reduce risk and keep control of your investment goals.</p>
      <h2 class="lessons-heading">Its many vital lessons include:</h2>
      <ul class="lessons">
        <li>How to keep your own home safe and out of the bank’s hands.</li>
        <li>The first step to successful investing is knowing where you want to finish. Learn how different exit strategies affect your investment plan.</li>
        <li>The main reason most Australians aren’t wealthy is that they don’t know the difference between appreciating and depreciating assets and beneficial and non-beneficial liabilities. Learn to view everything as one or the other.</li>
        <li>Grasping the concept of leverage and other people’s money will dramatically increase your return on equity.</li>
        <li>Banking and finance. By knowing what lenders need to asses a loan, you can apply with confidence and put yourself ahead of the pack.</li>
      </ul>
    </div>

    <div class="publisher"><span class="publisher-dot"></span>Harbour Keystone</div>
  </section>

  <div class="band">
    <span class="contact phone">1300 555 018</span>
    <span class="contact web">www.harbourkeystone.com.au</span>
    <span class="tagline">The quiet road to plenty</span>
  </div>

  <section class="front-cover">
    <div class="front-title">
      <div class="title-kicker">The pocket handbook of</div>
      <div class="title-main">home<br>lending</div>
    </div>
    <div class="illustration front-illustration" role="img" aria-label="Large green 3D house outline rising into an upward arrow with a sweeping green curve"></div>
    <div class="author">Ned Pargiter</div>
  </section>
</main>
</body>
</html>
```